Cedar Hollow Business Card and Logo

Nutrition and Wellness Store Front. I sell supplements, herbs, tinctures, Loose Leaf Teas, natural snacks and drinks including gluten free. classes: Fitness; health and wellness; community health and wellness hub. It is a "shabby chic" store front. It is white and my accent color is turqouise I will be adding some jewelry, stones and rocks and jewelery. I am a Certified Herbalist and Certified Nutrition and Wellness Consultant, a Solvane Practitioner and Kavora instructor.

Target Market(s)

health and wellness seekers, fitness, baby boomer

Industry/Entity Type

Business

Contact Information for Business Card

Cedar Hollow Nutrition and Wellness
Marla Dunstable Certified Herbalist , Certified Nutrition and Wellness Consultant, Solvane Practitioner, Kavora Instructor

Font styles to use
Serif

Colors
33a6d7
3176b5
33b8a4

Requirements
Must have
• A picture that represents two mountain peaks with a floral accent.

```html
<!DOCTYPE html>
<html lang="en">
<head>
<meta charset="utf-8">
<title>Cedar Hollow Nutrition and Wellness – Business Card Options</title>
<link rel="stylesheet" href="https://fonts.googleapis.com/css2?family=Fondamento&family=Indie+Flower&family=Italianno&display=swap">
<style>
  :root {
    --page: #ffffff;
    --teal-light: #5bc0d6;
    --teal-light-line: #3fb2cc;
    --teal-deep: #00a9bd;
    --teal-deep-line: #0a8f9f;
    --teal-band: #0fa8b8;
    --outline-red: #b22a2e;
    --outline-grey: #4f6b70;
    --white: #ffffff;
    --ink-soft: #6ccbe0;
    --ink-mid: #3fb7cf;
    --ink-deep: #00a3b6;
  }

  * { box-sizing: border-box; margin: 0; padding: 0; }

  html, body {
    width: 877px;
    height: 1200px;
    overflow: hidden;
    background: var(--page);
  }

  .sheet { position: relative; width: 877px; height: 1200px; }

  .card {
    position: absolute;
    width: 415px;
    height: 242px;
    border: 1.5px solid var(--outline-grey);
    overflow: hidden;
  }
  .card::before {
    content: "";
    position: absolute;
    inset: 7px;
    border: 1.5px solid var(--teal-light-line);
    pointer-events: none;
    z-index: 2;
  }

  .col-left  { left: 11px; }
  .col-right { left: 450px; }
  .row-1 { top: 60px; }
  .row-2 { top: 341px; }
  .row-3 { top: 617px; }
  .row-4 { top: 897px; }

  .card--light { background: var(--teal-light); }
  .card--white { background: var(--white); border-color: var(--outline-red); }
  .card--deep  { background: var(--teal-deep); }
  .card--deep::before { border-color: var(--teal-deep-line); }
  .card--red-edge { border-color: var(--outline-red); }

  /* lotus artwork area */
  .flower-art {
    position: absolute;
    left: 50%;
    top: 38px;
    width: 190px;
    height: 128px;
    transform: translateX(-50%);
    border-radius: 50% 50% 46% 46% / 62% 62% 38% 38%;
  }
  .flower-art--white-on-light {
    background: radial-gradient(ellipse at 50% 60%, rgba(255,255,255,0.9) 0%, rgba(255,255,255,0.55) 45%, rgba(255,255,255,0.15) 100%);
  }
  .flower-art--white-on-deep {
    background: radial-gradient(ellipse at 50% 60%, rgba(255,255,255,0.85) 0%, rgba(255,255,255,0.45) 50%, rgba(255,255,255,0.1) 100%);
  }
  .flower-art--soft-ink {
    background: radial-gradient(ellipse at 50% 60%, var(--ink-mid) 0%, var(--ink-soft) 50%, rgba(108,203,224,0.2) 100%);
  }
  .flower-art--deep-ink {
    background: radial-gradient(ellipse at 50% 60%, var(--ink-deep) 0%, #35bccb 55%, rgba(0,163,182,0.2) 100%);
  }

  .business-name {
    position: absolute;
    left: 0;
    right: 0;
    text-align: center;
    white-space: nowrap;
    color: var(--white);
    line-height: 1;
    z-index: 1;
  }
  .card--white .business-name { color: var(--teal-light); }
  .card--white.card--deep-ink .business-name { color: var(--teal-deep); }

  .name--classic {
    top: 180px;
    font-family: "Fondamento", serif;
    font-size: 21px;
  }
  .name--hand {
    top: 184px;
    font-family: "Indie Flower", cursive;
    font-size: 24px;
  }
  .name--formal {
    font-family: "Italianno", serif;
    font-size: 29px;
  }

  /* ornate card: title above paired flowers and flourishes */
  .card--ornate .name--formal { top: 76px; }
  .ornament-art {
    position: absolute;
    left: 36px;
    right: 36px;
    top: 110px;
    height: 100px;
  }
  .ornament-art__flourish {
    position: absolute;
    inset: 20px 0 0 0;
    border-radius: 50% 50% 45% 45% / 30% 30% 70% 70%;
    background: radial-gradient(ellipse at 50% 100%, rgba(255,255,255,0.35), rgba(255,255,255,0.05) 70%);
  }
  .ornament-art__bloom {
    position: absolute;
    top: 6px;
    width: 72px;
    height: 60px;
    border-radius: 50% 50% 46% 46% / 62% 62% 38% 38%;
    background: radial-gradient(ellipse at 50% 60%, rgba(255,255,255,0.85), rgba(255,255,255,0.2));
  }
  .ornament-art__bloom--left  { left: 88px; }
  .ornament-art__bloom--right { right: 88px; }

  /* banded card */
  .card--banded { border-color: var(--teal-deep-line); }
  .card--banded .flower-art { top: 26px; width: 200px; height: 136px; }
  .name-band {
    position: absolute;
    left: 0;
    right: 0;
    bottom: 0;
    height: 64px;
    background: var(--teal-band);
  }
  .card--banded .name--formal { top: 193px; font-size: 31px; }
</style>
</head>
<body>
<main class="sheet">

  <section class="card card--light col-left row-1">
    <div class="flower-art flower-art--white-on-light" role="img" aria-label="White line illustration of a lotus flower"></div>
    <p class="business-name name--classic">Cedar Hollow Nutrition and Wellness</p>
  </section>

  <section class="card card--white col-right row-1">
    <div class="flower-art flower-art--soft-ink" role="img" aria-label="Light turquoise line illustration of a lotus flower"></div>
    <p class="business-name name--classic">Cedar Hollow Nutrition and Wellness</p>
  </section>

  <section class="card card--light card--red-edge col-left row-2">
    <div class="flower-art flower-art--white-on-light" role="img" aria-label="White line illustration of a lotus flower"></div>
    <p class="business-name name--hand">Cedar Hollow Nutrition and Wellness</p>
  </section>

  <section class="card card--white col-right row-2">
    <div class="flower-art flower-art--soft-ink" role="img" aria-label="Light turquoise line illustration of a lotus flower"></div>
    <p class="business-name name--hand">Cedar Hollow Nutrition and Wellness</p>
  </section>

  <section class="card card--deep col-left row-3">
    <div class="flower-art flower-art--white-on-deep" role="img" aria-label="White line illustration of a lotus flower"></div>
    <p class="business-name name--hand">Cedar Hollow Nutrition and Wellness</p>
  </section>

  <section class="card card--white card--deep-ink col-right row-3">
    <div class="flower-art flower-art--deep-ink" role="img" aria-label="Deep turquoise line illustration of a lotus flower"></div>
    <p class="business-name name--hand">Cedar Hollow Nutrition and Wellness</p>
  </section>

  <section class="card card--deep card--red-edge card--ornate col-left row-4">
    <p class="business-name name--formal">Cedar Hollow Nutrition and Wellness</p>
    <div class="ornament-art" role="img" aria-label="Two small lotus flowers framed by curling white flourishes">
      <span class="ornament-art__flourish"></span>
      <span class="ornament-art__bloom ornament-art__bloom--left"></span>
      <span class="ornament-art__bloom ornament-art__bloom--right"></span>
    </div>
  </section>

  <section class="card card--light card--banded col-right row-4">
    <div class="flower-art flower-art--white-on-light" role="img" aria-label="White line illustration of a lotus flower"></div>
    <div class="name-band"></div>
    <p class="business-name name--formal">Cedar Hollow Nutrition and Wellness</p>
  </section>

</main>
</body>
</html>
```